Spectacular Business Card Design for AI SAAS Plattform called Leapvine.ai

Hi Creators
I need an outstanding new Design for my business card.
I run an AI automated Saas Plattform Called Leapvine.ai

Front side:
Logo
Slogan: DIY Business Development & Social Media Management
Data:
Name: Markus Obelwinter - CEO / Founder
email: m.obelwinter@leapvine.ai
mobile: +43 699 82 37 415

Company name:
Leapvine FlexCo

Backside:

What we stand for Slogan:
Vertrauen in KI-Technologie, getragen von menschlicher Vision: Dein Sprung nach vorn!
+ a fancy design what captures our core competencies - AI automisations, Social Media Management, Business development
(dont know if its too much, but AI and social media should be )

pls find attached the logo and the old design

Industry/Entity Type

AI automations for marketing and business development

Contact Information for Business Card

Front side: Logo Slogan: DIY Business Development & Social Media Management Data: Name: Markus Obelwinter - CEO / Founder email: m.obelwinter@leapvine.ai mobile: +43 699 82 37 415 Company name: Leapvine FlexCo Backside: What we stand for Slogan: Vertrauen in KI-Technologie, getragen von menschlicher Vision: Dein Sprung nach vorn!

Font styles to use
Serif
Sans Serif

Requirements
Nice to have
• a fancy design on the backside, a fancy design what captures our core competencies - AI automisations, Social Media Management, Business development

```html
<!DOCTYPE html>
<html lang="de">
<head>
<meta charset="utf-8">
<title>Leapvine.ai – Visitenkarte</title>
<link rel="stylesheet" href="https://fonts.googleapis.com/css2?family=Open+Sans:wght@400;600;700&family=Oswald:wght@300&display=swap">
<style>
  :root {
    --teal: #0b86a1;
    --teal-deep: #0a7f9c;
    --olive: #8a8e62;
    --orange: #f28c28;
    --orange-warm: #ee8a2e;
    --ink: #333333;
    --paper: #ffffff;
    --stage: #c9c9c9;
  }
  * { margin: 0; padding: 0; box-sizing: border-box; }
  html, body {
    width: 1200px; height: 900px; overflow: hidden;
    background: var(--stage);
    font-family: "Open Sans", Arial, sans-serif;
  }
  .sheet {
    width: 1200px; height: 900px;
    display: flex; flex-direction: column;
    align-items: center; justify-content: center; gap: 40px;
  }
  .card {
    position: relative;
    width: 700px; height: 400px;
    border-radius: 34px;
    overflow: hidden;
  }

  /* Rückseite */
  .card--back {
    background: linear-gradient(20deg, var(--teal-deep) 0%, #3e8d8a 38%, var(--olive) 60%, var(--orange-warm) 88%);
    color: var(--paper);
  }
  .card--back .wordmark {
    position: absolute; left: 80px; top: 70px;
    display: flex; align-items: center; gap: 22px;
    font-size: 72px; font-weight: 600; letter-spacing: 1px;
  }
  .wordmark__square {
    width: 40px; height: 40px; background: currentColor; display: inline-block;
  }
  .card--back .mission {
    position: absolute; left: 80px; top: 210px;
    font-size: 19px; line-height: 1.5;
  }
  .card--back .mission__claim { font-weight: 700; font-size: 22px; }
  .card--back .competencies {
    position: absolute; left: 80px; bottom: 52px;
    display: flex; gap: 34px;
    font-size: 19px;
  }

  /* Vorderseite */
  .card--front { background: var(--paper); }
  .card--front .wordmark {
    position: absolute; left: 60px; top: 54px;
    display: flex; align-items: center; gap: 18px;
    font-size: 64px; font-weight: 600; color: var(--teal);
  }
  .card--front .wordmark__square { width: 34px; height: 34px; background: var(--orange); }
  .tagline {
    position: absolute; left: 62px; top: 146px;
    font-family: "Oswald", "Arial Narrow", sans-serif;
    font-weight: 300; font-size: 25px; color: var(--ink);
  }
  .person { position: absolute; left: 62px; top: 218px; }
  .person__name { font-size: 36px; font-weight: 700; line-height: 1.1; }
  .person__first { color: var(--teal); }
  .person__last { color: var(--orange); }
  .person__role { font-size: 20px; color: var(--ink); margin-top: 2px; }
  .contact {
    position: absolute; left: 62px; bottom: 40px;
    list-style: none; font-size: 21px; color: var(--ink);
  }
  .contact li { display: flex; align-items: center; gap: 12px; line-height: 1.45; }
  .contact svg { width: 22px; height: 22px; fill: var(--teal); flex: none; }
  .company {
    position: absolute; right: 46px; bottom: 40px;
    font-size: 16px; font-weight: 600; color: var(--teal);
  }
  .accent-band {
    position: absolute; right: 0; top: 0; width: 260px; height: 100%;
    background: linear-gradient(160deg, rgba(242,140,40,0.10), rgba(11,134,161,0.12));
  }
</style>
</head>
<body>
<main class="sheet">

  <section class="card card--back" aria-label="Rückseite">
    <div class="wordmark"><span class="wordmark__square"></span>Leapvine</div>
    <p class="mission">
      Vertrauen in KI-Technologie, getragen von menschlicher<br>
      <span class="mission__claim">Dein Sprung nach vorn!</span>
    </p>
    <p class="competencies">
      <span>AI automisations</span>
      <span>Social Media Management</span>
      <span>Business development</span>
    </p>
  </section>

  <section class="card card--front" aria-label="Vorderseite">
    <div class="accent-band"></div>
    <div class="wordmark"><span class="wordmark__square"></span>Leapvine</div>
    <p class="tagline">DIY Business Development &amp; Social Media Management</p>
    <div class="person">
      <p class="person__name"><span class="person__first">Markus</span> <span class="person__last">Obelwinter</span></p>
      <p class="person__role">CEO / Founder</p>
    </div>
    <ul class="contact">
      <li>
        <svg viewBox="0 0 24 24" aria-hidden="true"><path d="M6.6 10.8a15.1 15.1 0 0 0 6.6 6.6l2.2-2.2a1 1 0 0 1 1-.25 11.4 11.4 0 0 0 3.6.57 1 1 0 0 1 1 1V20a1 1 0 0 1-1 1A17 17 0 0 1 3 4a1 1 0 0 1 1-1h3.5a1 1 0 0 1 1 1c0 1.25.2 2.45.57 3.57a1 1 0 0 1-.25 1z"/></svg>
        +43 699 82 37 415
      </li>
      <li>
        <svg viewBox="0 0 24 24" aria-hidden="true"><path d="M2 5h20v14H2zm2 2v.4l8 5.1 8-5.1V7zm0 2.8V17h16V9.8l-8 5.1z"/></svg>
        m.obelwinter@leapvine.ai
      </li>
    </ul>
    <p class="company">Leapvine FlexCo</p>
  </section>

</main>
</body>
</html>
```